PowerPoint Listing Presentation

I am a real estate agent with Branford Oakes Realty in the Las Vegas, Nevada market. I want a power point presentation that I can use with sellers who are considering the sale of their home. This presentation should include the following:
1. Charts and graphs about home sales statistics in the market.
2. Company Logo
3. My photo
4. A graphical description of where buyers come from
5. A graphical description of correct pricing strategies that sell
6. Pages that illustrate the things I do to sell homes.
7. A page that I can change with my personal statistics of annual sales numbers
8. A page that I can change with my personal market statistics as compared to the local association member’s average statistics.
9. Other pages with some graphics, photos and places for me to add data as needed.
Some of my stats:
1. I am a Broker licensed in Nevada since 1987
2. I average over 130 closed home sales per year.
3. I sell my listings in an average of 50 days at 103.52% of list price
4 The average property sells in 63 days at 100.27% of list price.
5. My team is made up of me, an executive assistant, marketing coordinator, buyer specialists, listing specialists

Target Market(s)

Prospective sellers of residential real estate

Industry/Entity Type

Real Estate

Requirements
Nice to have
• Places where I can edit and make changes to graphs, charts and text to make sure the presentation stays consistent with my stats and that of the market.

```html
<!DOCTYPE html>
<html lang="en">
<head>
<meta charset="utf-8">
<title>Listing Presentation – Selling Your Home</title>
<link href="https://fonts.googleapis.com/css2?family=Open+Sans:wght@400;700&family=Arimo:wght@400;700&display=swap" rel="stylesheet">
<style>
  :root {
    --bg-dark: #2b2b2b;
    --band-light: #3b3b3b;
    --band-mid: #333333;
    --swoosh: #ffffff;
    --swoosh-edge: #c9ced6;
    --rule-blue: #3d6fb5;
    --rule-glow: #8fb3e4;
    --rule-deep: #27528f;
    --title-top: #e9eef4;
    --title-bottom: #a9b6c6;
    --bullet-text: #ffffff;
    --frame: #efefef;
    --frame-shadow: rgba(0,0,0,0.55);
    --photo-sky: #b9cde0;
    --photo-stone: #c9aa86;
    --photo-garden: #5f7a3e;
    --footer-black: #121212;
    --footer-text: #ffffff;
    --brand-ink: #1a1a1a;
  }
  * { margin: 0; padding: 0; box-sizing: border-box; }
  html, body { width: 1200px; height: 900px; overflow: hidden; background: var(--bg-dark); }
  .slide {
    position: relative;
    width: 1200px;
    height: 900px;
    overflow: hidden;
    font-family: "Open Sans", sans-serif;
    background: repeating-linear-gradient(
      to bottom,
      var(--band-mid) 0px, var(--band-mid) 38px,
      var(--band-light) 38px, var(--band-light) 74px,
      var(--bg-dark) 74px, var(--bg-dark) 110px
    );
  }
  .swoosh { position: absolute; top: 0; right: 0; width: 460px; height: 100px; }
  .brand {
    position: absolute;
    top: 14px;
    right: 26px;
    width: 186px;
    height: 56px;
    display: flex;
    align-items: center;
    gap: 8px;
  }
  .brand-mark { width: 14px; height: 14px; background: var(--brand-ink); flex: none; }
  .brand-name {
    font-weight: 700;
    font-size: 16px;
    line-height: 1.15;
    color: var(--brand-ink);
  }
  .slide-title {
    position: absolute;
    left: 72px;
    top: 70px;
    font-size: 56px;
    line-height: 76px;
    font-weight: 700;
    background: linear-gradient(to bottom, var(--title-top), var(--title-bottom));
    -webkit-background-clip: text;
    background-clip: text;
    color: transparent;
    filter: drop-shadow(2px 3px 2px rgba(0,0,0,0.6));
    white-space: nowrap;
  }
  .title-rule {
    position: absolute;
    left: 62px;
    top: 151px;
    width: 1080px;
    height: 9px;
    background: linear-gradient(to bottom, var(--rule-glow), var(--rule-blue) 50%, var(--rule-deep));
    border-radius: 2px;
  }
  .points {
    position: absolute;
    left: 84px;
    top: 218px;
    width: 500px;
    list-style: none;
  }
  .points li {
    position: relative;
    padding-left: 36px;
    color: var(--bullet-text);
    font-weight: 700;
    font-size: 24px;
    line-height: 56px;
    margin-bottom: 17px;
  }
  .points li svg { position: absolute; left: 0; top: 19px; width: 18px; height: 18px; }
  .photo-frame {
    position: absolute;
    left: 645px;
    top: 206px;
    width: 501px;
    height: 519px;
    background: var(--frame);
    padding: 20px 19px 17px 20px;
    box-shadow: 4px 6px 10px var(--frame-shadow);
  }
  .house-photo {
    width: 100%;
    height: 100%;
    background: linear-gradient(to bottom, var(--photo-sky) 0%, var(--photo-stone) 40%, var(--photo-stone) 62%, var(--photo-garden) 100%);
  }
  .footer-curve { position: absolute; left: 0; bottom: 0; width: 530px; height: 135px; }
  .agent-photo {
    position: absolute;
    left: 59px;
    top: 819px;
    width: 60px;
    height: 56px;
    background: linear-gradient(to bottom, #6a6a6a, #2a2a2a);
  }
  .agent-card {
    position: absolute;
    left: 138px;
    top: 818px;
    font-family: "Arimo", sans-serif;
    font-size: 14px;
    line-height: 18px;
    color: var(--footer-text);
  }
</style>
</head>
<body>
<div class="slide">
  <svg class="swoosh" viewBox="0 0 460 100" preserveAspectRatio="none" aria-hidden="true">
    <path d="M0 0 H460 V100 H250 C160 92 80 50 0 0 Z" fill="var(--swoosh-edge)"/>
    <path d="M30 0 H460 V94 H260 C170 86 95 46 30 0 Z" fill="var(--swoosh)"/>
  </svg>

  <div class="brand">
    <span class="brand-mark"></span>
    <span class="brand-name">Branford Oakes<br>Realty</span>
  </div>

  <h1 class="slide-title">Selling Your Home</h1>
  <div class="title-rule"></div>

  <ul class="points">
    <li><svg viewBox="0 0 18 18"><path d="M1 1 L17 9 L1 17 L5 9 Z" fill="#fff" stroke="#222" stroke-width="1"/></svg>Nevada Broker since 1987, serving Las Vegas sellers</li>
    <li><svg viewBox="0 0 18 18"><path d="M1 1 L17 9 L1 17 L5 9 Z" fill="#fff" stroke="#222" stroke-width="1"/></svg>130+ closed home sales a year</li>
    <li><svg viewBox="0 0 18 18"><path d="M1 1 L17 9 L1 17 L5 9 Z" fill="#fff" stroke="#222" stroke-width="1"/></svg>My listings sell in 50 days</li>
    <li><svg viewBox="0 0 18 18"><path d="M1 1 L17 9 L1 17 L5 9 Z" fill="#fff" stroke="#222" stroke-width="1"/></svg>At 103.52% of list price</li>
    <li><svg viewBox="0 0 18 18"><path d="M1 1 L17 9 L1 17 L5 9 Z" fill="#fff" stroke="#222" stroke-width="1"/></svg>Market: 63 days at 100.27%</li>
    <li><svg viewBox="0 0 18 18"><path d="M1 1 L17 9 L1 17 L5 9 Z" fill="#fff" stroke="#222" stroke-width="1"/></svg>A full team behind your sale</li>
  </ul>

  <div class="photo-frame">
    <div class="house-photo" role="img" aria-label="Photo of a stone-and-stucco home with arched entry porch and landscaped front garden"></div>
  </div>

  <svg class="footer-curve" viewBox="0 0 530 135" preserveAspectRatio="none" aria-hidden="true">
    <path d="M0 4 C170 -8 370 30 530 135 H0 Z" fill="var(--footer-black)"/>
  </svg>
  <div class="agent-photo" role="img" aria-label="Agent headshot"></div>
  <div class="agent-card">
    Dale Harmon<br>
    Broker Licensed Nevada<br>
    Since 1987
  </div>
</div>
</body>
</html>
```